Erstellung von Datenblatt-Template
Zielgruppe
Informationen über ins finden Sie hier:
https://www.tovrel-de.de/unternehmen
Aufgabenstellung
Bitte erstellen Sie anhand von den folgenden Produkten:
Produkt A: https://www.tovrel-de.de/produkte/flexible-led-leisten/flexible-led-leiste-kalt-weiss-mit-flat-top-leds
Produkt B: https://www.tovrel-de.de/produkte/lagerartikel/led-einheit-rq71-5w
Datenblatt-Templates. Produkt A hat 3 Bilder und viel Text und Produkt B hat 1 Bild und wenig Text. Bei Produkt A fügen Sie bitte noch einen Platzhalter für eine Kurzbeschreibung hinzu, um “viel Text” zu simulieren.
Wichtig ist, dass es für uns zukünftig einfach ist dieses Template zu bearbeiten um Datenblätter für all unsere Produkte selber erstellen zu können. Hier sollten uns dann mehrere Templates zur Auswahl stehen (Typ A: viel Text, Typ B: wenig Text. Des Weiteren soll es die Möglichkeit geben die Anzahl der Bilder einfach zu bestimmen (mindestens 1, höchstens 3).
Bitte beschreiben Sie auch kurz wie die Bearbeitung auf unserer Seite aussehen würde, wenn wir uns für dieses Template entscheiden würden. Dies soll so einfach wie möglich gestaltet sein, da wir nur einfache Bearbeitungen wie Text/Bilder einfügen oder ähnliches vornehmen können.
Das Template soll professionell und übersichtlich sein. Die Farbkombinationen sind Ihnen überlassen, jedoch bitte nicht allzu bunt. Im Datenblatt sollen folgende Informationen angegeben sein:
• Überschrift: Produktdatenblatt
• Name des Produktes
• Produktbild/Bilder
• Kurzbeschreibung des Produktes
• Technische Daten (Als Tabelle)
• Eine Auswahl aus den Icons „Icons.zip“ im Anhang (welche Icons bei welchem Produkt angezeigt werden sollte dann auch von uns definierbar sein):
• Footer mit Firmenlogo (im Anhang) und Kontaktdaten (Daten: https://www.tovrel-de.de/impressum)

```html
<!DOCTYPE html>
<html lang="de">
<head>
<meta charset="utf-8">
<title>Produktdatenblatt – LED-Einheit RQ71-5W</title>
<link rel="stylesheet" href="https://fonts.googleapis.com/css2?family=Roboto+Condensed:wght@400;500&family=Arimo:wght@400;700&display=swap">
<style>
  :root {
    --accent: #8e1a45;
    --band: #e3e3e3;
    --panel: #ebebeb;
    --ink: #1a1a1a;
    --rule: #3a3a3a;
    --photo: #f2efea;
  }
  * { box-sizing: border-box; margin: 0; padding: 0; }
  html, body { width: 849px; height: 1200px; overflow: hidden; background: #fff; }
  body { position: relative; font-family: "Arimo", Arial, sans-serif; color: var(--ink); }

  .brand { position: absolute; left: 640px; top: 88px; display: flex; align-items: center; gap: 8px; }
  .brand-dot { width: 12px; height: 12px; border-radius: 50%; background: var(--accent); }
  .brand-name { font-family: "Arimo", Arial, sans-serif; font-size: 19px; color: var(--accent); letter-spacing: .5px; }

  .doc-title { position: absolute; left: 81px; top: 76px; font-family: "Roboto Condensed", sans-serif; font-weight: 400; font-size: 34px; letter-spacing: .3px; }

  .product-band { position: absolute; left: 0; top: 126px; width: 541px; height: 32px; background: var(--band); border-bottom: 3px solid var(--accent); }
  .product-name { position: absolute; left: 81px; top: 8px; font-family: "Roboto Condensed", sans-serif; font-size: 18px; }

  .intro { position: absolute; left: 81px; top: 189px; width: 689px; font-size: 12.3px; line-height: 16px; text-align: justify; }

  .spec { position: absolute; left: 81px; top: 305px; width: 459px; border-collapse: collapse; font-size: 12.6px; line-height: 15.5px; }
  .spec th { width: 144px; text-align: left; font-weight: 400; vertical-align: top; padding: 12px 0 0 6px; border-bottom: 1px solid var(--rule); }
  .spec td { background: var(--panel); vertical-align: top; padding: 10px 0 0 16px; border-bottom: 1px solid var(--rule); border-left: 3px solid #fff; }
  .spec tr:first-child td { border-top: 4px solid var(--accent); }
  .row-name th, .row-name td { height: 48px; }
  .row-info th, .row-info td { height: 415px; }
  .row-marks th, .row-marks td { height: 90px; }

  .features { list-style: none; }
  .features li { position: relative; padding-left: 13px; margin-bottom: 7px; }
  .features li::before { content: ""; position: absolute; left: 0; top: 4px; width: 8px; height: 8px; background: var(--accent); }

  .badge { margin-top: 102px; width: 56px; height: 56px; border-radius: 50%; border: 2px solid #555; background: #fff; }
  .mark { margin-top: 8px; width: 48px; height: 48px; border: 2px solid #222; border-radius: 7px; background: #fff; }

  .photo-frame { position: absolute; left: 579px; top: 305px; width: 270px; height: 265px; border: 1px solid var(--accent); background: #fff; padding: 10px; }
  .photo { width: 100%; height: 100%; background: linear-gradient(160deg, var(--photo), #e4ddd3 60%, #f5f3f0); }

  .footer { position: absolute; left: 0; top: 1110px; width: 849px; height: 90px; background: var(--band); border-top: 4px solid var(--accent); text-align: center; font-size: 12.4px; line-height: 16px; padding-top: 10px; }
  .footer .company { font-weight: 700; margin-bottom: 4px; }
</style>
</head>
<body>
  <div class="brand"><span class="brand-dot"></span><span class="brand-name">Tovrel Lichtwerk</span></div>

  <h1 class="doc-title">PRODUKTDATENBLATT</h1>
  <div class="product-band"><h2 class="product-name">LED-EINHEIT RQ71-5W</h2></div>

  <p class="intro">Soluptae eum ipis volentotam, quid ut aliquas sa nobis dolut aspedit que se seritam, et autatur? Bisqui abor as aut quatatu rerovid quias ped magnimus es sitium laciatur, verum adio. Odi dolupta sumquo consequam inus quae nis ipis reptas es same dolorepudae vellant ad quae ventium hictam inumquos re cum enderum quam volesto officite con nonseque comni bea vit eiunti doluptatus Ati isci occus expliam eum es rempore conseque alibero qui aditium nis dios raercillant estent poratiisci dit et qui consequi dolorio nsecepro bearci quam.</p>

  <table class="spec">
    <tr class="row-name">
      <th>Produktbezeichnung</th>
      <td>LED-Einheit RQ71-5W</td>
    </tr>
    <tr class="row-info">
      <th>Produktinformation</th>
      <td>
        <ul class="features">
          <li>5 Leuchtdioden Ø 5 mm wasserklar transparent weiß blinkend (ultrahell).</li>
          <li>Sequenzblinkfunktion</li>
          <li>Blinkdauer ca. 2 Monate im Dauerbetrieb mit 3 Mignonzellen Voltaro Alkaline.</li>
          <li>Kabellänge zu jeder LED ca. 40 cm, am Batteriehalter ca. 30 cm, Toleranz der Kabellängen +/- 10 %.</li>
          <li>Steuerplatine 55 x 24 mm, Batteriehalter ca. 58 x 47 x 17 mm, LED-Platinen 12 x 26 mm.</li>
          <li>Batteriehalter und alle Platinen mit geschäumten Selbstklebe-Stanzteilen vorkonfektioniert.</li>
        </ul>
        <div class="badge" role="img" aria-label="Lieferzeit-Kennzeichen"></div>
      </td>
    </tr>
    <tr class="row-marks">
      <th>Prüfzeichen</th>
      <td><div class="mark" role="img" aria-label="Prüfzeichen"></div></td>
    </tr>
  </table>

  <div class="photo-frame">
    <div class="photo" role="img" aria-label="Produktfoto: LED-Einheit mit Steuerplatine, fünf LED-Platinen an Kabeln und Batteriehalter"></div>
  </div>

  <footer class="footer">
    <div class="company">Tovrel Lichtwerk – Elektronische Werbemittel GmbH</div>
    <div>Lindenring 14 | 50321 Brühl | Germany</div>
    <div>Telefon: 02232 - 48 17 20 | Fax: 02232 - 48 17 221 | E-Mail: info@tovrel-de.de | www.tovrel-de.de</div>
    <div>Geschäftsführer: Jonas Berthold | Amtsgericht Köln, HRB 4873 | Umsatzsteuer-ID: DE305718246 | WEEE-Reg.-Nr.: DE 61490275</div>
  </footer>
</body>
</html>
```